Detox Poster Design Project

I am a naturopath that works in Melbourne. I require a poster that I can put up in my natural therapies clinic that is advertising a detox program that I am offering. The program runs for 3 or 6 weeks and is designed to help your liver, gut and kidney cleanse toxins more efficiently, leaving you feeling energised and healthy.

I would like to see designs that are fresh, organic, clear and contemporary to look at. I want to sell the idea of feeling good, wellbeing and vitality to the potential client. Colours I like include greens, greys and blues.

The final design should communicate health and happiness.

Requirements
Must have
• Please include the photo of the woman in nature.Poster size will be A2 594mm by 420mm
Nice to have
• I have attached the design work for my business cards that you can use. It would be great if the colours and style are in keeping with the existing design work for my business. I have also attached an extra image (almond milk photo) just in case you could see a use for it.

Many thanks.
Should not have
• No hippy, new age looking design.

```html
<!DOCTYPE html>
<html lang="en">
<head>
<meta charset="utf-8">
<title>Detox Program Poster</title>
<link rel="stylesheet" href="https://fonts.googleapis.com/css2?family=Playfair+Display:wght@400&family=Rokkitt:wght@300;400&display=swap">
<style>
  :root {
    --paper: #ffffff;
    --trim: #e23ee0;
    --forest: #2f6a2b;
    --forest-deep: #24561f;
    --leaf: #6cc04a;
    --leaf-light: #8fd46a;
    --band-text: #2b3a24;
    --text-light: #f3f7ef;
    --photo-bright: #dfe9d2;
    --photo-mid: #7fa56a;
    --photo-dark: #3f6a34;
  }
  * { margin: 0; padding: 0; box-sizing: border-box; }
  html, body {
    width: 1200px; height: 860px; overflow: hidden;
    background: var(--paper);
  }
  .poster {
    position: relative; width: 1200px; height: 860px;
    background: var(--paper);
    font-family: "Rokkitt", Georgia, serif;
  }
  .trim-line {
    position: absolute; left: 29px; width: 1141px; height: 1px;
    background: var(--trim);
  }
  .trim-line--top { top: 26px; }
  .trim-line--bottom { top: 824px; }
  .hero-photo {
    position: absolute; left: 29px; top: 27px; width: 1141px; height: 797px;
    background:
      radial-gradient(ellipse 260px 340px at 330px 520px, rgba(230,225,210,0.55), transparent 70%),
      linear-gradient(160deg, var(--photo-bright) 0%, var(--photo-mid) 35%, var(--photo-dark) 70%, var(--photo-mid) 100%);
  }
  .info-panel {
    position: absolute; left: 559px; top: 27px; width: 567px; height: 797px;
    background: radial-gradient(ellipse at 50% 30%, var(--forest) 0%, var(--forest-deep) 100%);
    color: var(--text-light);
    text-align: center;
  }
  .emblem {
    position: absolute; left: 238px; top: 88px; width: 90px; height: 130px;
    border-radius: 45px 45px 8px 8px;
    background: linear-gradient(180deg, var(--leaf-light), var(--leaf));
    opacity: 0.85;
  }
  .title {
    position: absolute; left: 0; right: 0; top: 228px;
    font-family: "Playfair Display", Georgia, serif;
    font-size: 90px; line-height: 1; letter-spacing: 6px;
    color: transparent;
    -webkit-text-stroke: 2px var(--leaf-light);
  }
  .summary {
    position: absolute; left: 40px; right: 40px; top: 353px;
    font-size: 24px; line-height: 34.5px; font-weight: 300;
  }
  .practitioner-band {
    position: absolute; left: 552px; top: 556px; width: 584px; height: 122px;
    background: var(--leaf);
    color: var(--band-text);
    text-align: center;
  }
  .practitioner-name {
    margin-top: 24px; font-size: 33px; font-weight: 300; line-height: 1.1;
  }
  .practitioner-credential {
    margin-top: 6px; font-size: 20px; font-weight: 300; color: var(--text-light);
  }
  .contact {
    position: absolute; left: 0; right: 0; top: 676px;
  }
  .contact-phone { font-size: 40px; font-weight: 300; line-height: 1.1; }
  .contact-email { margin-top: 8px; font-size: 18px; font-weight: 300; }
  .side-photo-tab {
    position: absolute; left: 94px; top: 774px; width: 109px; height: 50px;
    background: var(--leaf);
  }
  .side-photo {
    position: absolute; left: 70px; top: 642px; width: 150px; height: 150px;
    border-radius: 50%;
    border: 4px solid var(--paper);
    background: radial-gradient(circle at 40% 45%, #f6f3ee 0%, #e8ddcf 55%, #c99a6f 100%);
  }
</style>
</head>
<body>
<main class="poster">
  <div class="hero-photo" role="img" aria-label="Photo of a woman seen from behind with arms raised in a lush green rainforest"></div>

  <section class="info-panel">
    <div class="emblem" role="img" aria-label="Green lotus flower emblem"></div>
    <h1 class="title">DETOX</h1>
    <p class="summary">The program runs for<br>3 or 6 weeks and is designed to help<br>your liver, gut and kidney cleanse<br>toxins more efficiently, leaving you<br>feeling energised and healthy.</p>
    <div class="contact">
      <p class="contact-phone">T: 0400 123 456</p>
      <p class="contact-email">E: hello@clarawhitfield.com.au</p>
    </div>
  </section>

  <section class="practitioner-band">
    <p class="practitioner-name">Clara Whitfield B.A. B.H.Sc.</p>
    <p class="practitioner-credential">(Naturopathy) Member ANPG</p>
  </section>

  <div class="side-photo-tab"></div>
  <div class="side-photo" role="img" aria-label="Round photo of a glass of almond milk with almonds"></div>

  <div class="trim-line trim-line--top"></div>
  <div class="trim-line trim-line--bottom"></div>
</main>
</body>
</html>
```